Buch-/eBook-Cover für Liebesroman
Zielgruppe
Ich bin Autorin und suche ein Cover für mein neues Buch. Meine Zielgruppe sind junge Erwachsene, die Liebesromane lesen.
Aufgabenstellung
Der Titel ist 'Als ob ein Regen durch die Stille fällt' und als Autorin soll Margarete Hollweck draufstehen.
Ich mag Cover, auf denen keine Menschen bzw. nicht der komplette Mensch zu sehen ist. Farbentechnisch würde ich mich überraschen lassen, solange es nicht zu bunt wird. :-) Als Schriftart darf es gern eine Schreibschrift sein. Ich lasse mich aber auch zu etwas anderem überreden, wenn es zum restlichen Cover passt. ;-)
Das Cover sollte eine Auflösung von mind. 300 dpi haben (gern mehr) und möglichst im jpg-Format sein.
Der Inhalt des Buches: Es geht um ein Männerpaar. Der eine ist verheiratet (mit einer Frau) und verliebt sich in seinen Kumpel. Die beiden beginnen eine Affäre, woraus aber bald mehr wird. Am Ende trennt er sich von seiner Frau und entscheidet sich für seinen Kumpel.
Es ist ein Liebesroman, aber das Cover sollte trotzdem nicht zu klischeehaft sein.
Da ich das hier nicht anders auswählen kann, noch eine kleine Anmerkung. Ich möchte nach Möglichkeit keine Stockmaterialien im Cover haben.

```html
<!DOCTYPE html>
<html lang="de">
<head>
<meta charset="utf-8">
<title>Als ob ein Regen durch die Stille fällt – Margarete Hollweck</title>
<link rel="stylesheet" href="https://fonts.googleapis.com/css2?family=Arvo&family=Allison&display=swap">
<style>
  :root {
    --stage: #f2d8bb;
    --paper: #f2f2f2;
    --ink: #111111;
    --peach: #f2d6b6;
    --salmon: #f0a896;
    --blush: #f8c3b6;
    --sand: #f5dcc8;
    --rose: #f0bfb6;
  }
  html, body {
    margin: 0;
    padding: 0;
    width: 1200px;
    height: 1200px;
    overflow: hidden;
    background: var(--stage);
  }
  .cover {
    position: absolute;
    left: 207px;
    top: 39px;
    width: 786px;
    height: 1122px;
    background: var(--paper);
    overflow: hidden;
  }
  .cover__art {
    position: absolute;
    inset: 0;
    width: 786px;
    height: 1122px;
  }
  .cover__author,
  .cover__title-line {
    position: absolute;
    margin: 0;
    font-family: "Arvo", Georgia, serif;
    font-weight: 400;
    color: var(--ink);
    text-transform: uppercase;
    white-space: nowrap;
  }
  .cover__author {
    top: 82px;
    left: 0;
    right: 0;
    text-align: center;
    font-size: 31px;
    letter-spacing: 0.2em;
  }
  .cover__title {
    margin: 0;
    font-weight: 400;
  }
  .cover__title-line {
    font-size: 31px;
    letter-spacing: 0.18em;
  }
  .cover__title-line--top {
    left: 122px;
    top: 740px;
  }
  .cover__title-line--bottom {
    right: 96px;
    top: 1044px;
  }
  .cover__title-script {
    position: absolute;
    left: 0;
    right: 0;
    top: 770px;
    text-align: center;
    font-family: "Allison", "Brush Script MT", cursive;
    font-size: 196px;
    line-height: 1.1;
    color: var(--ink);
    white-space: nowrap;
  }
</style>
</head>
<body>
  <article class="cover">
    <svg class="cover__art" viewBox="0 0 786 1122" role="img"
         aria-label="Feine Einlinienzeichnung eines Schmetterlings, der über einer geöffneten Hand schwebt, auf weichen Farbflächen in Pfirsich, Lachs und Rosé">
      <path class="blob blob--sand-left" fill="var(--sand)" opacity="0.85"
            d="M0 470 C70 455 160 470 200 560 C220 610 230 650 290 665 C330 675 325 720 290 730 C240 745 190 725 140 720 C80 712 40 725 0 735 Z"/>
      <path class="blob blob--blush-left" fill="var(--blush)" opacity="0.75"
            d="M30 470 C45 440 90 438 140 450 C185 462 210 490 198 520 C185 550 150 562 110 560 C60 558 25 545 26 515 C26 495 26 482 30 470 Z"/>
      <path class="blob blob--peach" fill="var(--peach)"
            d="M440 142 C500 135 540 185 524 250 C515 290 540 320 565 360 C590 400 580 440 530 470 C480 500 440 505 410 485 C380 465 370 420 370 360 C372 270 390 150 440 142 Z"/>
      <path class="blob blob--salmon" fill="var(--salmon)" opacity="0.85"
            d="M250 305 C300 285 360 310 420 365 C470 410 490 470 478 520 C468 555 430 575 395 560 C365 548 360 520 340 505 C315 487 280 490 255 470 C220 445 205 400 215 355 C222 330 235 312 250 305 Z"/>
      <path class="blob blob--rose-right" fill="var(--rose)" opacity="0.85"
            d="M786 448 C745 448 700 470 688 515 C678 560 705 585 735 600 C760 612 770 650 775 690 L786 725 Z"/>
      <path class="blob blob--sand-right" fill="var(--sand)" opacity="0.85"
            d="M786 625 C735 635 675 665 662 715 C652 770 690 820 740 842 C760 850 775 852 786 852 Z"/>
    </svg>

    <p class="cover__author">Margarete Hollweck</p>

    <h1 class="cover__title">
      <span class="cover__title-line cover__title-line--top">Als ob ein Regen</span>
      <span class="cover__title-script">durch die Stille</span>
      <span class="cover__title-line cover__title-line--bottom">fällt</span>
    </h1>
  </article>
</body>
</html>
```